Book Cover Project

This is a printed journal front and back cover design. We like the current design, but it feels a little too flat / too simple.

NOTE: we are not looking for a total makeover, just a finishing / polishing of this cover.

Here is our other book cover: https://www.shelvorix.com/Mat-Studio-Blueprint-Calm-Days/dp/7390462815/ref=tmm_hrd_swatch_0?_encoding=UTF8&qid=&sr=
it's purple and yellow (mostly purple)
this one is yellow and we're thinking to add a purple bar at the bottom

Specs: 6 in x 9 in full bleed for print

```html
<!DOCTYPE html>
<html lang="en">
<head>
<meta charset="utf-8">
<title>Kinetic Distance Notebook – Cover</title>
<link rel="stylesheet" href="https://fonts.googleapis.com/css2?family=Arimo:ital,wght@0,700;1,700&display=swap">
<style>
  :root {
    --cover-yellow: #ffd500;
    --brand-purple: #5156a6;
    --title-black: #0a0a0a;
    --runner-tone-a: #5a5fb0;
    --runner-tone-b: #e0c22a;
  }
  html, body {
    margin: 0;
    padding: 0;
    overflow: hidden;
    background: var(--cover-yellow);
  }
  .cover {
    position: relative;
    width: 805px;
    height: 1200px;
    overflow: hidden;
    background: var(--cover-yellow);
    font-family: "Arimo", Arial, sans-serif;
  }
  .title-line,
  .tagline {
    position: absolute;
    left: 0;
    width: 100%;
    margin: 0;
    text-align: center;
    line-height: 1;
    font-weight: 700;
    white-space: nowrap;
  }
  .title-line {
    color: var(--title-black);
    letter-spacing: 1px;
    z-index: 2;
  }
  .title-line--first { top: 272px; font-size: 120px; }
  .title-line--second { top: 491px; font-size: 124px; }
  .title-line--third { top: 717px; font-size: 110px; }

  .tagline {
    color: var(--brand-purple);
    font-style: italic;
    font-size: 50px;
    letter-spacing: 3px;
  }
  .tagline--run { top: 405px; }
  .tagline--write { top: 646px; }
  .tagline--transform { top: 863px; }

  .runner-slot {
    position: relative;
    display: inline-block;
    width: 0.45em;
    height: 1em;
    vertical-align: top;
  }
  .runner-figure {
    position: absolute;
    left: -6px;
    top: -180px;
    width: 70px;
    height: 400px;
    border-radius: 35px;
    background: linear-gradient(180deg, var(--runner-tone-a) 0%, var(--runner-tone-a) 60%, var(--runner-tone-b) 100%);
    opacity: 0.6;
    z-index: -1;
  }
  .sr-only {
    position: absolute;
    width: 1px;
    height: 1px;
    overflow: hidden;
    clip: rect(0 0 0 0);
    white-space: nowrap;
  }

  .author-bar {
    position: absolute;
    left: 0;
    bottom: 0;
    width: 100%;
    height: 105px;
    background: var(--brand-purple);
  }
  .author-name {
    position: absolute;
    left: 0;
    width: 100%;
    top: 37px;
    margin: 0;
    text-align: center;
    line-height: 1;
    font-size: 32px;
    font-weight: 700;
    letter-spacing: 5px;
    color: var(--cover-yellow);
  }
</style>
</head>
<body>
  <main class="cover">
    <h1 class="title-line title-line--first">K<span class="runner-slot"><span class="runner-figure" role="img" aria-label="Single-line drawing of a runner in a purple vest and shorts, standing in for the letter I"></span><span class="sr-only">I</span></span>NETIC</h1>
    <p class="tagline tagline--run">RUN</p>
    <p class="title-line title-line--second">DISTANCE</p>
    <p class="tagline tagline--write">WRITE</p>
    <p class="title-line title-line--third">NOTEBOOK</p>
    <p class="tagline tagline--transform">TRANSFORM</p>
    <footer class="author-bar">
      <p class="author-name">ELIAS THORNBURY</p>
    </footer>
  </main>
</body>
</html>
```